Strategic Plan Notecards (4.25in x 5.5 in)

I need a design for project cards that will be handed out to the general public as part of a Strategic Planning effort for a client. I'd like the cards to be 4.25 x 5.5 so that they can be printed 4 to a US letter-size sheet of paper.

The Project title is "City of Quellmont Strategic Plan Update"
Needs to include text:

For more info, go to www.quellmontfutures.example
Take the Vision Survey at http://lnk.example/QuellmontOutlook
What do YOU want Quellmont to be?

Other variations on this text will be considered.

Target Market(s)

General Public

Font styles to use
Serif
Sans Serif

Colors

Designer to choose colors to be used in the design.

Requirements
Must have
• An interesting and fun visual appeal. Nothing stuffy. Should have a bright graphic background and interesting typefaces for the text.
Nice to have
• One of the biggest assets in the community is the Missouri River - some depiction of a river would be great.

```html
<!DOCTYPE html>
<html lang="en">
<head>
<meta charset="utf-8">
<title>City of Quellmont Strategic Plan Update</title>
<link href="https://fonts.googleapis.com/css2?family=Anton&family=Oswald:wght@500;600&family=Pathway+Gothic+One&display=swap" rel="stylesheet">
<style>
  :root {
    --forest: #2f8a42;
    --sunflower: #f6c026;
    --river-blue: #21739a;
    --ember: #e2622a;
    --cream: #ebedc6;
    --ink: #111;
  }
  html, body {
    margin: 0;
    padding: 0;
    overflow: hidden;
    background: #fff;
  }
  .card {
    position: relative;
    width: 1200px;
    height: 903px;
    background: var(--forest);
    overflow: hidden;
  }
  .plan-title {
    position: absolute;
    left: 28px;
    top: 10px;
    margin: 0;
    font-family: "Oswald", sans-serif;
    font-weight: 600;
    font-size: 68px;
    line-height: 1.1;
    letter-spacing: 1px;
    text-transform: lowercase;
    color: var(--cream);
    white-space: nowrap;
  }
  .state-map {
    position: absolute;
    left: 48px;
    top: 104px;
    width: 1084px;
    height: 660px;
  }
  .vision-question {
    position: absolute;
    left: 0;
    top: 0;
    margin: 0;
    font-family: "Anton", sans-serif;
    font-weight: 400;
    text-transform: lowercase;
    text-shadow: 4px 5px 6px rgba(0, 0, 0, 0.45);
  }
  .vision-question .line {
    position: absolute;
    white-space: nowrap;
    line-height: 1;
  }
  .line-one { left: 128px; top: 282px; font-size: 136px; color: var(--river-blue); }
  .line-two { left: 30px; top: 438px; font-size: 136px; color: var(--river-blue); }
  .accent { color: var(--ember); }
  .accent-big { font-size: 168px; color: var(--ember); }
  .contact {
    position: absolute;
    left: 28px;
    margin: 0;
    font-family: "Pathway Gothic One", sans-serif;
    font-size: 56px;
    line-height: 1;
    text-transform: lowercase;
    color: var(--ink);
    white-space: nowrap;
    -webkit-text-stroke: 0.8px currentColor;
  }
  .contact .link { color: var(--cream); }
  .contact-info { top: 770px; }
  .contact-survey { top: 836px; }
</style>
</head>
<body>
  <main class="card">
    <h1 class="plan-title">City of Quellmont Strategic Plan Update</h1>

    <svg class="state-map" viewBox="0 0 1084 660" role="img" aria-label="Map of the state with the river winding through it and a star marking Quellmont">
      <rect width="1084" height="660" fill="var(--sunflower)"/>
    </svg>

    <h2 class="vision-question">
      <span class="line line-one">What do <span class="accent-big">YOU</span> want</span>
      <span class="line line-two"><span class="accent">Quellmont</span> to be?</span>
    </h2>

    <p class="contact contact-info">for more info, go to <span class="link">www.quellmontfutures.example</span></p>
    <p class="contact contact-survey">take the vision survey at <span class="link">http://lnk.example/QuellmontOutlook</span></p>
  </main>
</body>
</html>
```